Start up Dialysis Clinic needs its first website - Velmora Health

Create a visually appealing and user-friendly website for Velmora Health, a dialysis clinic located in Mt. Irvine, Tobago. The website should effectively communicate our services to local, regional, and international patients, providing essential information and fostering trust and engagement..
Key Goals:

1. Informative: Provide comprehensive information about our services, facility, and team.
2. User-Friendly: Ensure the website is easy to navigate, with a clear structure and accessible content.
3. Engaging: Create a visually appealing design that reflects the professionalism and care of Velmora Health.
4. Responsive: Ensure the website is fully responsive and performs well on all devices, including desktops, tablets, and smartphones.
5. Trust-Building: Include testimonials, credentials, and patient resources to build trust with potential patients.
Scope of Work:

1. Home Page: An inviting and informative landing page that provides an overview of our clinic, mission, and services. Include a call to action for more information and contact details.
2. About Us: A detailed page about Velmora Health, including our mission, vision, team, and facility tour.
3. Services: A comprehensive page describing the dialysis services we offer, including Hemodialysis, Peritoneal Dialysis, and Home Hemodialysis.
4. Patient Information: A resourceful section with guides for new patients, FAQs, insurance and billing information, and downloadable forms.
5. Resources: Educational content about kidney health, dialysis options, diet and nutrition tips, and support groups.
6. Contact Us: A contact page with our address, phone number, email, office hours, a contact form, and a map.

```html
<!DOCTYPE html>
<html lang="en">
<head>
<meta charset="utf-8">
<title>Velmora Health – Dialysis Clinic</title>
<link href="https://fonts.googleapis.com/css2?family=Open+Sans:wght@400;600;700&display=swap" rel="stylesheet">
<style>
:root{
  --navy:#0f1b45;
  --navy-deep:#0c1235;
  --blue:#2b5f9e;
  --blue-mid:#3a6fae;
  --green:#4f9a36;
  --green-light:#6aae45;
  --ink:#1a1f36;
  --muted:#8a90a0;
  --line:#dfe3ea;
  --white:#ffffff;
  --bg-soft:#f7f8fa;
  --grad:linear-gradient(90deg,var(--blue) 0%,var(--green) 100%);
}
*{margin:0;padding:0;box-sizing:border-box}
html,body{width:1200px;height:4186px;overflow:hidden}
body{font-family:"Open Sans",Arial,sans-serif;color:var(--ink);background:var(--white);position:relative}
.abs{position:absolute}
svg{display:block}

/* header */
.topbar{left:472px;top:0;width:728px;height:32px;background:var(--navy);display:flex;align-items:center;gap:36px;padding-left:100px;color:#fff;font-size:12px;font-weight:600}
.topbar::before{content:"";position:absolute;left:-30px;top:0;border-top:32px solid var(--navy);border-left:30px solid transparent}
.topbar span{display:flex;align-items:center;gap:10px}
.ring{width:24px;height:24px;border:1.5px solid #fff;border-radius:50%;display:flex;align-items:center;justify-content:center}
.brand{left:130px;top:14px;display:flex;align-items:center;gap:10px}
.brand-mark{width:20px;height:20px;background:var(--blue);display:block}
.brand-name{font-weight:700;font-size:20px;color:var(--blue);letter-spacing:.3px;white-space:nowrap}
.nav{left:486px;top:55px;display:flex;font-size:11px;font-weight:600;white-space:nowrap}
.nav a{color:var(--ink);text-decoration:none;position:relative;display:block}
.nav a.active{color:var(--blue)}
.nav a.active::after{content:"";position:absolute;left:-4px;width:44px;top:32px;height:3px;background:var(--grad)}
.social{left:908px;top:50px;display:flex;gap:14px}
.social i{width:24px;height:24px;border:1.5px solid var(--blue);border-radius:50%;display:block}

/* hero */
.hero{left:0;top:89px;width:1200px;height:724px;background:linear-gradient(100deg,#13275f 0%,#2c4b86 38%,#8fa2c2 70%,#c9d3e2 100%)}
.hero-tag{left:122px;top:281px;width:266px;height:44px;background:var(--navy-deep);border-left:3px solid var(--green);color:#fff;font-size:21px;font-weight:600;padding:10px 0 0 20px}
.hero-title{left:116px;top:330px;color:#fff;font-size:64px;font-weight:700;letter-spacing:1px}
.hero-text{left:122px;top:424px;width:440px;color:#fff;font-size:17px;line-height:26px}
.btn{background:var(--grad);color:#fff;font-weight:700;display:flex;align-items:center;justify-content:center;gap:10px}
.hero-btn{left:122px;top:523px;width:176px;height:50px;font-size:16px}

/* about */
.label{font-size:12px;font-weight:600;color:var(--blue);padding-bottom:4px;border-bottom:2px solid var(--green);display:inline-block;letter-spacing:.3px}
.photo{background:linear-gradient(180deg,#eef1f5 0%,#d4dbe5 100%)}
.h2{font-size:37px;font-weight:700;line-height:46px;color:var(--ink)}
.body-sm{font-size:12px;line-height:19px;color:var(--muted)}

/* services */
.svc-card{background:#fff;text-align:center;padding-top:26px}
.svc-card h3{font-size:17px;font-weight:700;margin-top:22px;margin-bottom:10px}
.svc-card p{font-size:13px;line-height:20px;color:var(--muted);padding:0 44px}
.icon-disc{width:82px;height:82px;border-radius:50%;background:var(--grad);margin:0 auto;display:flex;align-items:center;justify-content:center}
.svc-card.featured{background:linear-gradient(160deg,#5a9e3c,#6fae4a);color:#fff}
.svc-card.featured p{color:#eef5e8}
.svc-card.featured .icon-disc{background:#fff}

/* features */
.feature{background:#fff;box-shadow:0 2px 10px rgba(20,30,60,.08);display:flex;padding:22px 0 0 20px;gap:16px}
.feature h4{font-size:16px;font-weight:600;color:var(--ink);opacity:.85;margin-bottom:6px}
.feature p{font-size:12.5px;line-height:20px;color:var(--muted)}

/* appointment */
.field{background:#fff;border:1px solid var(--line);font-size:13px;color:var(--ink);display:flex;align-items:center;gap:9px;padding-left:16px}
.field.area{align-items:flex-start;padding-top:12px}

/* steps */
.step{width:220px;height:220px;border-radius:50%;background:#fff;box-shadow:0 6px 18px rgba(20,30,60,.12);text-align:center}
.step .top{position:absolute;left:53px;top:-101px;width:114px;height:114px;border-radius:50%;background:#fff;display:flex;align-items:center;justify-content:center}
.step .top .icon-disc{width:114px;height:114px}
.step .num{position:absolute;left:96px;top:0;width:28px;height:28px;border-radius:50%;background:#fff;color:var(--blue);font-size:12px;font-weight:700;display:flex;align-items:center;justify-content:center;box-shadow:0 1px 4px rgba(0,0,0,.08)}
.step h4{margin-top:42px;font-size:14px;font-weight:700;color:var(--blue)}
.step p{font-size:9.5px;line-height:13px;color:var(--ink);padding:6px 22px 0}
.step a{display:block;margin-top:10px;font-size:9px;color:var(--blue);text-decoration:none;font-weight:600}
.step.featured{background:linear-gradient(135deg,var(--blue),var(--green))}
.step.featured h4,.step.featured p,.step.featured a{color:#fff}

/* footer */
.footer{left:0;top:3788px;width:1200px;height:342px;background:var(--navy-deep)}
.foot-brand{left:0;width:1200px;top:3796px;display:flex;flex-direction:column;align-items:center;gap:12px}
.foot-brand .brand-mark{width:60px;height:60px}
.foot-brand .brand-name{font-size:32px;line-height:40px;color:var(--blue-mid)}
.foot-nav{left:296px;top:3948px;display:flex;color:#fff;font-size:15px;white-space:nowrap}
.foot-nav span{display:block}
.foot-rule{left:142px;top:4000px;width:917px;height:1px;background:#3a4168}
.contact{display:flex;align-items:center;gap:16px;color:#fff;font-size:12px;line-height:18px}
.contact .ring{width:56px;height:56px;border-color:#cfd3e0}
.vsep{width:1px;height:60px;background:#3a4168}
.bottombar{left:0;top:4130px;width:1200px;height:56px;background:var(--grad);color:#fff;font-size:13px;font-weight:600;display:flex;align-items:center;padding-left:147px}
.sq{width:24px;height:24px;border:1.5px solid #fff;display:block}
</style>
</head>
<body>

<!-- Header -->
<div class="abs topbar">
  <span><span class="ring"><svg width="12" height="12" viewBox="0 0 24 24" fill="none" stroke="#fff" stroke-width="2.4"><path d="M5 3h4l2 5-3 2a12 12 0 0 0 6 6l2-3 5 2v4a2 2 0 0 1-2 2A17 17 0 0 1 3 5a2 2 0 0 1 2-2z"/></svg></span>CALL US TODAY : (123) 456-7890</span>
  <span><span class="ring"><svg width="12" height="12" viewBox="0 0 24 24" fill="none" stroke="#fff" stroke-width="2.4"><rect x="3" y="5" width="18" height="14"/><path d="M3 6l9 7 9-7"/></svg></span>EMAIL: info@company.com</span>
</div>
<div class="abs brand"><i class="brand-mark"></i><span class="brand-name">Velmora Health</span></div>
<nav class="abs nav">
  <a class="active" href="#" style="width:93px">HOME</a><a href="#" style="width:94px">Solutions</a><a href="#" style="width:93px">About Us</a><a href="#" style="width:92px">Contact Us</a><a href="#">FAQs</a>
</nav>
<div class="abs social"><i></i><i></i><i></i><i></i></div>

<!-- Hero -->
<div class="abs hero" role="img" aria-label="Photo of a doctor and a nurse in masks reviewing a clipboard in a clinic corridor"></div>
<svg class="abs" style="left:0;top:680px" width="1200" height="140" viewBox="0 0 1200 140">
  <path d="M0 40 C300 150 800 130 1200 20 L1200 140 L0 140Z" fill="var(--blue)"/>
  <path d="M0 48 C300 150 800 128 1200 40 L1200 140 L0 140Z" fill="var(--green)"/>
  <path d="M0 55 C300 158 800 135 1200 55 L1200 140 L0 140Z" fill="#fff"/>
</svg>
<div class="abs hero-tag">We are experts in</div>
<div class="abs hero-title">Dialysis</div>
<p class="abs hero-text">Lorem ipsum dolor sit amet, consectetur adipiscing elit, sed do eiusmod tempor incididunt ut labore et dolore magna aliqua.</p>
<div class="abs btn hero-btn">Read More</div>

<!-- About -->
<div class="abs photo" style="left:163px;top:878px;width:325px;height:480px;border-radius:160px 160px 0 0" role="img" aria-label="Photo of a smiling male doctor holding a stethoscope"></div>
<div class="abs" style="left:610px;top:902px"><span class="label">WHO WE ARE</span></div>
<h2 class="abs h2" style="left:610px;top:936px">Embrace the journey,<br>see the results</h2>
<p class="abs" style="left:610px;top:1054px;font-size:18px;font-weight:600">Transform your body, transform your life.</p>
<p class="abs body-sm" style="left:610px;top:1092px;width:454px">Lorem ipsum dolor sit amet, consectetur adipiscing elit, sed do eiusmod temp or incididunt ut labore et dolore magna aliqua. Ut enim ad minim veniam, quis laboris nisi ut aliquip ex ea commodo consequat.</p>
<p class="abs body-sm" style="left:610px;top:1161px;width:454px">Lorem ipsum dolor sit amet, consectetur adipiscing elit, sed do eiusmod temp or incididunt ut labore et dolore magna aliqua.</p>
<div class="abs btn" style="left:610px;top:1224px;width:136px;height:39px;font-size:14px">Contact us <svg width="16" height="12" viewBox="0 0 16 12" fill="none" stroke="#fff" stroke-width="1.6"><path d="M0 6h14M9 1l5 5-5 5"/></svg></div>

<!-- Services -->
<svg class="abs" style="left:0;top:1330px" width="1200" height="560" viewBox="0 0 1200 560" role="img" aria-label="Dark blue tinted photo of medical staff at work">
  <defs><linearGradient id="svcbg" x1="0" x2="1"><stop offset="0" stop-color="#1c2550"/><stop offset="1" stop-color="#2a3564"/></linearGradient></defs>
  <path d="M0 70 Q600 -40 1200 70 L1200 556 L0 556Z" fill="url(#svcbg)"/>
</svg>
<div class="abs" style="left:0;width:1200px;top:1397px;text-align:center"><span class="label" style="color:#fff;border-color:#fff">OUR SERVICES</span></div>
<h2 class="abs" style="left:0;width:1200px;top:1436px;text-align:center;font-size:42px;font-weight:600;color:#fff">Services We Provide</h2>
<div class="abs svc-card" style="left:164px;top:1538px;width:290px;height:267px">
  <div class="icon-disc"><svg width="40" height="40" viewBox="0 0 40 40" fill="none" stroke="#fff" stroke-width="2"><path d="M6 28a14 14 0 1 1 28 0"/><path d="M20 28l6-10"/><circle cx="20" cy="28" r="2"/></svg></div>
  <h3>Hemodialysis</h3><p>Lorem ipsum dolor sit amet, con sectetur adipiscing elit, sed do eiusmod tem</p>
</div>
<div class="abs svc-card" style="left:740px;top:1538px;width:284px;height:267px">
  <div class="icon-disc"><svg width="40" height="40" viewBox="0 0 40 40" fill="none" stroke="#fff" stroke-width="2"><path d="M8 32h24M14 32l4-12 8-6M22 10a4 4 0 1 1 6 5"/></svg></div>
  <h3>Home Hemodialysis</h3><p>Lorem ipsum dolor sit amet, con sectetur adipiscing elit, sed do eiusmod tem</p>
</div>
<div class="abs svc-card featured" style="left:453px;top:1520px;width:287px;height:301px;padding-top:44px" role="img" aria-label="Green tinted photo of dialysis equipment behind service card">
  <div class="icon-disc"><svg width="40" height="40" viewBox="0 0 40 40" fill="none" stroke="var(--green)" stroke-width="2"><path d="M20 7l12 9-5 14H13L8 16z"/><circle cx="20" cy="7" r="3"/><circle cx="32" cy="16" r="3"/><circle cx="27" cy="30" r="3"/><circle cx="13" cy="30" r="3"/><circle cx="8" cy="16" r="3"/></svg></div>
  <h3>Peritoneal Dialysis</h3><p>Lorem ipsum dolor sit amet, con sectetur adipiscing elit, sed do eiusmod tem</p>
</div>

<!-- Why choose us -->
<div class="abs" style="left:0;top:1886px;width:1200px;height:637px;background:var(--bg-soft)"></div>
<div class="abs photo" style="left:146px;top:1959px;width:423px;height:564px;border-radius:200px 200px 0 0" role="img" aria-label="Photo of a female doctor holding a tablet"></div>
<div class="abs" style="left:616px;top:1985px"><span class="label">WHY CHOOSE US</span></div>
<h2 class="abs h2" style="left:616px;top:2022px;font-size:41px;line-height:51px">Healthy Today,<br>Happier Tomorrow.</h2>
<div class="abs feature" style="left:602px;top:2151px;width:219px;height:98px"><svg width="30" height="30" viewBox="0 0 40 40" fill="none" stroke="var(--blue)" stroke-width="2"><path d="M8 32h24M14 32l4-12 8-6M22 10a4 4 0 1 1 6 5"/></svg><div><h4>Confidentiality</h4><p>Inventore veritasis uas<br>vitae dicta sunt</p></div></div>
<div class="abs feature" style="left:847px;top:2151px;width:220px;height:98px"><svg width="30" height="30" viewBox="0 0 40 40" fill="none" stroke="var(--blue)" stroke-width="2"><path d="M8 32h24M14 32l4-12 8-6M22 10a4 4 0 1 1 6 5"/></svg><div><h4>Client-centric</h4><p>Inventore veritasis uas<br>vitae dicta sunt</p></div></div>
<div class="abs feature" style="left:602px;top:2276px;width:219px;height:98px"><svg width="30" height="30" viewBox="0 0 40 40" fill="none" stroke="var(--blue)" stroke-width="2"><path d="M8 32h24M14 32l4-12 8-6M22 10a4 4 0 1 1 6 5"/></svg><div><h4>Professionalism</h4><p>Inventore veritasis uas<br>vitae dicta sunt</p></div></div>
<div class="abs feature" style="left:847px;top:2276px;width:220px;height:98px"><svg width="30" height="30" viewBox="0 0 40 40" fill="none" stroke="var(--blue)" stroke-width="2"><path d="M8 32h24M14 32l4-12 8-6M22 10a4 4 0 1 1 6 5"/></svg><div><h4>Proven Record</h4><p>Inventore veritasis uas<br>vitae dicta sunt</p></div></div>

<!-- Appointment -->
<svg class="abs" style="left:0;top:2523px" width="1200" height="512" viewBox="0 0 1200 512" role="img" aria-label="Dark blue tinted photo of a clinic room">
  <path d="M0 0 H1200 V440 Q600 540 0 440Z" fill="#27315b"/>
</svg>
<div class="abs" style="left:683px;top:2471px;width:455px;height:504px;background:linear-gradient(180deg,#3a4570,#1e2547);border-radius:220px 220px 0 0" role="img" aria-label="Photo of two smiling staff members in business suits"></div>
<h2 class="abs" style="left:130px;top:2612px;font-size:32px;font-weight:600;color:#fff">Request An Appointment</h2>
<div class="abs field" style="left:132px;top:2689px;width:231px;height:43px"><svg width="14" height="14" viewBox="0 0 24 24" fill="none" stroke="#333" stroke-width="2"><circle cx="12" cy="8" r="4"/><path d="M4 21a8 8 0 0 1 16 0"/></svg>Full Name</div>
<div class="abs field" style="left:390px;top:2689px;width:231px;height:43px"><svg width="14" height="14" viewBox="0 0 24 24" fill="none" stroke="#333" stroke-width="2"><rect x="3" y="4" width="18" height="16"/><circle cx="12" cy="10" r="3"/><path d="M7 18a5 5 0 0 1 10 0"/></svg>Email Address</div>
<div class="abs field" style="left:132px;top:2756px;width:231px;height:43px"><svg width="14" height="14" viewBox="0 0 24 24" fill="none" stroke="#333" stroke-width="2"><path d="M5 3h4l2 5-3 2a12 12 0 0 0 6 6l2-3 5 2v4a2 2 0 0 1-2 2A17 17 0 0 1 3 5a2 2 0 0 1 2-2z"/></svg>Phone</div>
<div class="abs field area" style="left:390px;top:2756px;width:231px;height:111px"><svg width="14" height="14" viewBox="0 0 24 24" fill="none" stroke="#333" stroke-width="2"><rect x="3" y="5" width="18" height="14"/><path d="M3 6l9 7 9-7"/></svg>Message</div>
<div class="abs field" style="left:132px;top:2824px;width:231px;height:43px"><svg width="14" height="14" viewBox="0 0 24 24" fill="none" stroke="#333" stroke-width="2"><path d="M4 17a9 9 0 1 1 16 0"/><path d="M12 15l4-5"/></svg>Date</div>
<div class="abs btn" style="left:132px;top:2886px;width:130px;height:37px;font-size:11.5px;font-weight:400">Request Now <svg width="10" height="9" viewBox="0 0 16 12" fill="none" stroke="#fff" stroke-width="2"><path d="M0 6h14M9 1l5 5-5 5"/></svg></div>

<!-- Steps -->
<div class="abs" style="left:0;top:3032px;width:1200px;height:760px;background:var(--bg-soft);z-index:-1"></div>
<div class="abs" style="left:0;width:1200px;top:3156px;text-align:center"><span class="label">STEPS TO TAKE</span></div>
<h2 class="abs" style="left:0;width:1200px;top:3192px;text-align:center;font-size:42px;font-weight:600">Steps to Take</h2>

<div class="abs step" style="left:123px;top:3345px">
  <div class="top"><div class="icon-disc"><svg width="44" height="44" viewBox="0 0 40 40" fill="none" stroke="#fff" stroke-width="2"><path d="M8 32h24M14 32l4-12 8-6M22 10a4 4 0 1 1 6 5"/></svg></div></div>
  <div class="num">1</div>
  <h4>Get in touch with us</h4><p>Lorem ipsum dolor sit amet, con sectetur adipiscing elit, sed do eiusmod tempor incididunt ut labore et dol ore magna aliqua. Ut</p><a href="#">Read More</a>
</div>
<div class="abs step featured" style="left:366px;top:3345px">
  <div class="top"><svg width="50" height="50" viewBox="0 0 40 40" fill="none" stroke="var(--blue)" stroke-width="2"><path d="M20 7l12 9-5 14H13L8 16z"/><circle cx="20" cy="7" r="3"/><circle cx="32" cy="16" r="3"/><circle cx="27" cy="30" r="3"/><circle cx="13" cy="30" r="3"/><circle cx="8" cy="16" r="3"/></svg></div>
  <div class="num">2</div>
  <h4>Speak to an Expert</h4><p>Lorem ipsum dolor sit amet, con sectetur adipiscing elit, sed do eiusmod tempor incididunt ut labore et dol ore magna aliqua. Ut</p><a href="#">Read More</a>
</div>
<div class="abs step" style="left:614px;top:3345px">
  <div class="top"><div class="icon-disc"><svg width="46" height="46" viewBox="0 0 40 40" fill="none" stroke="#fff" stroke-width="2"><path d="M6 28a14 14 0 1 1 28 0"/><path d="M20 28l6-10"/><circle cx="20" cy="28" r="2"/></svg></div></div>
  <div class="num">3</div>
  <h4>Schedule a meeting</h4><p>Lorem ipsum dolor sit amet, con sectetur adipiscing elit, sed do eiusmod tempor incididunt ut labore et dol ore magna aliqua. Ut</p><a href="#">Read More</a>
</div>
<div class="abs step" style="left:859px;top:3345px">
  <div class="top"><div class="icon-disc"><svg width="46" height="46" viewBox="0 0 40 40" fill="none" stroke="#fff" stroke-width="2"><circle cx="18" cy="18" r="12"/><path d="M6 18h24M18 6c-5 6-5 18 0 24M18 6c5 6 5 18 0 24"/><circle cx="29" cy="29" r="5"/></svg></div></div>
  <div class="num">4</div>
  <h4>Start Sessions</h4><p>Lorem ipsum dolor sit amet, con sectetur adipiscing elit, sed do eiusmod tempor incididunt ut labore et dol ore magna aliqua. Ut</p><a href="#">Read More</a>
</div>

<!-- Footer -->
<svg class="abs" style="left:0;top:3690px" width="1200" height="110" viewBox="0 0 1200 110">
  <path d="M0 110 C250 20 700 -20 1200 80 L1200 110Z" fill="var(--blue)"/>
  <path d="M0 110 C250 36 700 10 1200 110Z" fill="var(--green)"/>
  <path d="M0 110 C300 50 700 40 1200 110Z" fill="var(--navy-deep)"/>
</svg>
<div class="abs footer"></div>
<div class="abs foot-brand"><i class="brand-mark"></i><span class="brand-name">Velmora Health</span></div>
<div class="abs foot-nav"><span style="width:94px">HOME</span><span style="width:106px">SERVICES</span><span style="width:119px">ABOUT US</span><span style="width:149px">TESTIMONIALS</span><span>BLOG</span></div>
<div class="abs foot-rule"></div>
<div class="abs contact" style="left:142px;top:4049px"><span class="ring"><svg width="26" height="26" viewBox="0 0 24 24" fill="none" stroke="#fff" stroke-width="1.5"><circle cx="12" cy="12" r="9"/><path d="M3 12h18M12 3c-4 5-4 13 0 18M12 3c4 5 4 13 0 18"/></svg></span><span>123, Building Name, Street<br>City, State XY 123456</span></div>
<div class="abs vsep" style="left:398px;top:4050px"></div>
<div class="abs contact" style="left:474px;top:4049px"><span class="ring"><svg width="22" height="26" viewBox="0 0 20 26" fill="none" stroke="#fff" stroke-width="1.5"><rect x="4" y="2" width="12" height="22" rx="2"/><path d="M8 20h4"/></svg></span><span>PHONE<br>(123) 456 7890</span></div>
<div class="abs vsep" style="left:718px;top:4050px"></div>
<div class="abs contact" style="left:795px;top:4049px"><span class="ring"><svg width="26" height="26" viewBox="0 0 24 24" fill="none" stroke="#fff" stroke-width="1.5"><path d="M3 10l9-6 9 6v10H3z"/><path d="M3 10l9 6 9-6"/></svg></span><span>EMAIL<br>info@company.com</span></div>
<div class="abs bottombar">Velmora Health</div>
<div class="abs" style="left:933px;top:4146px;display:flex;gap:10px"><i class="sq"></i><i class="sq"></i><i class="sq"></i><i class="sq"></i></div>

</body>
</html>
```